Website for my photography business

I need a website for my photography business, Mira Quenell Photography. I need a website that has a landing page with a cover photo of each kind of photography I do. For example, Nature, Weddings, Portraits and Architecture. I want it so that when someone comes onto my website they have to choose which kind of photography page they want to visit. So if they click on the wedding photo it will open to a page with my wedding portfolio images and a contact me button. If they choose nature photography I want them to be redirected to an e-commerce section where they can purchase prints. Architecture and Portraits should open up to their respective portfolios with about me and contact info. I like this kind of format because I want people who come to my website for a specific type of photography to be able to be directed there easily without having to look at a mix of other kinds of photography. I will provide a few files to use as placeholders. I have already purchased the miraquenellphotography.com domain name. A Wix website would be great because I am most familiar with it but I am open to anything.

Industry/Entity Type

Photographer

Number of Pages Required

5+ page

Requirements
Must have
• Landing Page and e-commerce

```html
<!DOCTYPE html>
<html lang="en">
<head>
<meta charset="utf-8">
<title>Mira Quenell Photography</title>
<link rel="stylesheet" href="https://fonts.googleapis.com/css2?family=Josefin+Sans:wght@300;400;600;700&family=Montserrat:wght@600;700&family=Nunito+Sans:wght@700;800&display=swap">
<style>
  :root {
    --ink: #2b2b2b;
    --ink-soft: #555555;
    --accent: #b89a7c;
    --line: #d8d8d8;
    --white: #ffffff;
    --brand-ink: #2a2d4f;
  }
  * { margin: 0; padding: 0; box-sizing: border-box; }
  html, body { width: 1200px; height: 2333px; overflow: hidden; background: var(--white); }
  body { position: relative; font-family: "Josefin Sans", sans-serif; color: var(--ink); }
  .abs { position: absolute; }

  .brand { left: 0; width: 1200px; top: 58px; text-align: center;
    font-weight: 400; font-size: 26px; color: var(--brand-ink); letter-spacing: 1px; }
  .main-nav { top: 152px; left: 0; width: 1200px; display: flex; justify-content: center; }
  .main-nav a { font-family: "Montserrat", sans-serif; font-weight: 600; font-size: 10px; letter-spacing: 3.2px;
    color: var(--ink); text-decoration: none; margin: 0 22px; }

  .hero { top: 184px; left: 0; width: 1200px; height: 530px;
    background: linear-gradient(100deg, #7d6a5c 0%, #a8978a 30%, #b9a99b 50%, #c2a988 70%, #9c8e6e 100%); }
  .hero::after { content: ""; position: absolute; inset: 0; background: rgba(70,62,66,0.22); }
  .hero-copy { position: absolute; inset: 0; z-index: 1; text-align: center; color: var(--white); }
  .hero-kicker { position: absolute; top: 118px; width: 100%; font-weight: 400; font-size: 23px; line-height: 24px; }
  .hero-title { position: absolute; top: 190px; width: 100%; font-family: "Nunito Sans", sans-serif; font-weight: 800; font-size: 62px; line-height: 66px; letter-spacing: 1px; }
  .hero-text { position: absolute; top: 287px; left: 300px; width: 600px; font-weight: 300; font-size: 20px; line-height: 32px; }
  .see-more { position: absolute; top: 406px; left: 554px; font-family: "Montserrat", sans-serif; font-weight: 700; font-size: 9px; letter-spacing: 2.5px; display: flex; align-items: center; gap: 6px; }
  .see-more span { display: inline-block; width: 32px; height: 1px; background: var(--white); }

  .section-label { font-family: "Montserrat", sans-serif; font-weight: 700; font-size: 11px; letter-spacing: 2px; color: var(--ink); text-align: center; }
  .about-title { top: 789px; left: 0; width: 1175px; }
  .about-text { top: 828px; left: 350px; width: 475px; text-align: center; font-weight: 300; font-size: 16px; line-height: 25px; color: var(--ink-soft); letter-spacing: 0.5px; }
  .btn-hello { top: 957px; left: 529px; width: 118px; height: 34px; border: 1px solid var(--ink);
    font-family: "Montserrat", sans-serif; font-weight: 700; font-size: 9px; letter-spacing: 2.5px; display: flex; align-items: center; justify-content: center; }

  .category { top: 1073px; width: 390px; height: 513px; }
  .category .name { position: absolute; left: 0; right: 0; bottom: 50px; text-align: center; color: var(--white);
    font-family: "Josefin Sans", sans-serif; font-weight: 700; font-size: 27px; letter-spacing: 3px; }
  .cat-weddings { left: 7px; background: linear-gradient(165deg, #b6a898 0%, #8f7f70 50%, #6e625a 100%); }
  .cat-nature { left: 405px; background: linear-gradient(180deg, #3a4636 0%, #55604d 50%, #b9bcc2 75%, #e9ebf0 100%); }
  .cat-portraits { left: 803px; background: linear-gradient(160deg, #8a8a8a 0%, #6e6e6e 50%, #5a5a5a 100%); }
  .slider-arrow { top: 1290px; }

  .links { top: 1643px; }
  .link-item { position: absolute; text-align: center; width: 240px; }
  .link-item .title { font-weight: 600; font-size: 20px; letter-spacing: 4px; color: var(--ink); }
  .link-item .sub { margin-top: 14px; font-family: "Montserrat", sans-serif; font-weight: 700; font-size: 8px; letter-spacing: 2px; color: var(--ink); }
  .divider { width: 1px; height: 48px; background: var(--line); top: 1645px; }

  .follow-title { top: 1834px; left: 0; width: 1180px; text-align: center; font-weight: 600; font-size: 26px; letter-spacing: 3px; color: #3a3a3a; }
  .insta-strip { top: 1895px; left: 0; width: 1200px; height: 205px; display: flex; }
  .insta-strip div { flex: 1; }
  .tile-building { background: linear-gradient(180deg, #c9ccd0 0%, #a77d68 45%, #8e6b5a 75%, #7c8a5a 100%); }
  .tile-skin { background: linear-gradient(160deg, #8a8a8a, #6a6a6a); }
  .tile-fox { background: linear-gradient(180deg, #3a4636 0%, #5a634f 50%, #e9ebf0 100%); }
  .tile-ring { background: linear-gradient(165deg, #a99a8b, #7a6c60); }
  .insta-tag { top: 1991px; left: 430px; width: 263px; height: 37px; background: var(--white); display: flex; align-items: center; justify-content: center;
    font-family: "Montserrat", sans-serif; font-weight: 700; font-size: 8px; letter-spacing: 1.4px; color: var(--ink); }

  .footer-label { font-family: "Montserrat", sans-serif; font-weight: 700; font-size: 8px; letter-spacing: 1.8px; color: var(--accent); }
  .footer-text { font-weight: 400; font-size: 16px; letter-spacing: 0.8px; color: var(--ink-soft); }
  .studio-label { top: 2152px; left: 199px; }
  .studio-text { top: 2179px; left: 199px; }
  .phone-label { top: 2152px; right: 199px; }
  .phone-text { top: 2179px; right: 199px; }
  .footer-brand { top: 2178px; left: 450px; width: 272px; text-align: center; font-size: 18px; color: var(--brand-ink); }
</style>
</head>
<body>
  <header>
    <div class="abs brand">Mira Quenell Photography</div>
    <nav class="abs main-nav">
      <a href="#">HOME</a><a href="#">ABOUT</a><a href="#">PORTFOLIO</a><a href="#">SHOP</a><a href="#">BLOG</a><a href="#">CONTACT</a>
    </nav>
  </header>

  <section class="abs hero" role="img" aria-label="Cover photo of young women laughing outdoors in warm sunlight">
    <div class="hero-copy">
      <div class="hero-kicker">MIRA QUENELL</div>
      <div class="hero-title">PHOTOGRAPHY</div>
      <p class="hero-text">Lorem Ipsum is simply dummy text of the printing and typesetting industry. Lorem Ipsum has been the</p>
      <div class="see-more">SEE MORE <span></span></div>
    </div>
  </section>

  <h2 class="abs section-label about-title">ABOUT ME</h2>
  <p class="abs about-text">My greatest ambition is to create powerful images that commemorate, across generations, the people we love and the good times we have had. Creativity, hard work and experience are the engines that keep it all going.</p>
  <a class="abs btn-hello">SAY HELLO</a>

  <div class="abs category cat-weddings" role="img" aria-label="Wedding photo: rings resting on a speckled stone"><div class="name">WEDDINGS</div></div>
  <div class="abs category cat-nature" role="img" aria-label="Nature photo: wildlife in a snowy pine forest"><div class="name">NATURE</div></div>
  <div class="abs category cat-portraits" role="img" aria-label="Portrait photo: black and white figure study"><div class="name">PORTRAITS</div></div>

  <svg class="abs slider-arrow" style="left:30px" width="22" height="42" viewBox="0 0 22 42"><path d="M20 2 L3 21 L20 40" fill="none" stroke="#fff" stroke-opacity="0.75" stroke-width="2.5"/></svg>
  <svg class="abs slider-arrow" style="left:1138px" width="22" height="42" viewBox="0 0 22 42"><path d="M2 2 L19 21 L2 40" fill="none" stroke="#fff" stroke-opacity="0.75" stroke-width="2.5"/></svg>

  <div class="abs links">
    <div class="link-item" style="left:226px"><div class="title">PORTRAITS</div><div class="sub">BEST WORK</div></div>
    <div class="link-item" style="left:474px"><div class="title">JOURNAL</div><div class="sub">DAILY STORIES</div></div>
    <div class="link-item" style="left:718px"><div class="title">INVESTMENT</div><div class="sub">CHECK PRICES</div></div>
  </div>
  <div class="abs divider" style="left:472px"></div>
  <div class="abs divider" style="left:716px"></div>

  <h2 class="abs follow-title">FOLLOW US</h2>
  <div class="abs insta-strip">
    <div class="tile-building" role="img" aria-label="Brick campus building"></div>
    <div class="tile-skin" role="img" aria-label="Black and white figure study"></div>
    <div class="tile-fox" role="img" aria-label="Wildlife in snowy forest"></div>
    <div class="tile-ring" role="img" aria-label="Wedding rings on stone"></div>
    <div class="tile-building" role="img" aria-label="Brick campus building with trees"></div>
    <div class="tile-fox" role="img" aria-label="Wildlife in snow"></div>
  </div>
  <div class="abs insta-tag">INSTAGRAM @MIRA_QUENELL.PHOTOGRAPHER</div>

  <footer>
    <div class="abs footer-label studio-label">STUDIO</div>
    <div class="abs footer-text studio-text">Lorem sit amet, consectetur</div>
    <div class="abs footer-brand">Mira Quenell Photography</div>
    <div class="abs footer-label phone-label">PHONE</div>
    <div class="abs footer-text phone-text">00 (987) 210 43 65</div>
  </footer>
</body>
</html>
```